New Letterhead

Improve the attached letterhead to make it more alive and corporate class using the company colors in the two companies logos available on the two companies website.

Industry/Entity Type

Construction Company

Requirements
Must have
• colours of the two logod
Nice to have
• Be more alive and professional
Should not have
• Any other colours besides the ones in the logos

```html
<!DOCTYPE html>
<html lang="en">
<head>
<meta charset="utf-8">
<title>Letterhead</title>
<link href="https://fonts.googleapis.com/css2?family=Lato:wght@400;700;900&family=Open+Sans:wght@400;600&display=swap" rel="stylesheet">
<style>
  :root {
    --ink: #2b2e33;
    --body: #5a5a5a;
    --teal: #3a97a3;
    --maroon: #852a20;
    --paper: #ffffff;
  }
  * { margin: 0; padding: 0; box-sizing: border-box; }
  html, body { width: 1040px; height: 1200px; overflow: hidden; background: var(--paper); }
  .letterhead { position: relative; width: 1040px; height: 1200px; background: var(--paper); font-family: "Open Sans", sans-serif; color: var(--body); }
  .side-band { position: absolute; left: 0; top: 0; }
  .brand-row { position: absolute; left: 100px; top: 56px; display: flex; align-items: center; gap: 26px; font-family: "Lato", sans-serif; }
  .wordmark { display: flex; align-items: center; gap: 8px; font-weight: 900; letter-spacing: 0.5px; }
  .wordmark--primary { color: var(--ink); font-size: 46px; }
  .wordmark--primary .mark-square { width: 14px; height: 14px; background: var(--teal); }
  .wordmark--partner { color: var(--maroon); font-size: 26px; }
  .tagline { position: absolute; left: 705px; top: 76px; font-family: "Lato", sans-serif; font-weight: 700; font-size: 15px; line-height: 19px; color: #111; text-transform: uppercase; }
  .meta { position: absolute; left: 98px; font-size: 15px; line-height: 19px; }
  .issue-date { top: 195px; }
  .recipient { top: 232px; }
  .salutation { top: 336px; }
  .letter-body { position: absolute; left: 98px; top: 387px; width: 840px; font-size: 15.5px; line-height: 27.5px; text-align: justify; hyphens: auto; }
  .letter-body p + p { margin-top: 27px; }
  .closing { top: 794px; }
  .signatory { position: absolute; left: 98px; top: 870px; }
  .signatory-name { font-size: 19px; color: #333; font-weight: 600; }
  .signatory-role { font-size: 15px; margin-top: 6px; }
  .footer { position: absolute; left: 0; top: 1032px; width: 1040px; font-family: "Lato", sans-serif; font-size: 15px; line-height: 18px; color: #111; }
  .footer-col { position: absolute; top: 0; }
  .footer-col--primary { left: 100px; }
  .footer-col--partner { left: 372px; top: -2px; }
  .footer-col--legal { left: 697px; top: 52px; }
  .footer-divider { position: absolute; top: 0; width: 2px; height: 135px; background: var(--teal); }
  .footer-divider--a { left: 351px; }
  .footer-divider--b { left: 668px; }
  .entity--teal { color: var(--teal); }
  .entity--maroon { color: var(--maroon); }
  .contact { margin-top: 11px; }
  .directors { margin-top: 16px; }
  .directors .second { padding-left: 77px; display: block; }
</style>
</head>
<body>
<div class="letterhead">
  <svg class="side-band" width="22" height="1200" viewBox="0 0 22 1200" aria-hidden="true">
    <polygon points="0,0 22,0 22,505 0,522" fill="var(--ink)"/>
    <polygon points="0,530 22,513 22,948 0,965" fill="var(--teal)"/>
    <polygon points="0,973 22,956 22,1200 0,1200" fill="var(--maroon)"/>
  </svg>

  <div class="brand-row">
    <div class="wordmark wordmark--primary">KORVEL<span class="mark-square"></span></div>
    <div class="wordmark wordmark--partner">MABETA GROUP</div>
  </div>
  <div class="tagline">Building lasting value<br>on every site,<br>every day</div>

  <div class="meta issue-date">Issuing Date: May 5, 2018</div>
  <div class="meta recipient">Name Of Employee Mr. XYZABC<br>Address of Employee<br>Address Line 2 etc..</div>
  <div class="meta salutation">Dear Mr.XYZABC</div>

  <div class="letter-body">
    <p>Lorem Ipsum has been the industry's standard dummy text ever since the 1500s, when an unknown printer took a galley of type and scrambled it to make a type specimen book. It has survived not only five centuries, but also the leap into electronic typesetting, remaining essentially unchanged. It was popularised in the 1960s with the release of dry-transfer sheets containing Lorem Ipsum passages, and more recently with desktop publishing and layout software including versions of Lorem Ipsum.</p>
    <p>Lorem Ipsum is simply dummy text of the printing and typesetting industry. Lorem Ipsum has been the industry's standard dummy text ever since the 1500s, when an unknown printer took a galley of type and scrambled it to make a type specimen book.</p>
    <p>It has survived not only five centuries, but also the leap into electronic typesetting, remaining essentially unchanged. It was popularised in the 1960s with the release of dry-transfer sheets containing Lorem Ipsum passages.</p>
  </div>

  <div class="meta closing">Yours Sincerely</div>
  <div class="signatory">
    <div class="signatory-name">Daniel Moore</div>
    <div class="signatory-role">Managing Director</div>
  </div>

  <footer class="footer">
    <div class="footer-col footer-col--primary">
      <div class="entity--teal">Korvel MB JV (Pty) Limited</div>
      12 Alder Lane<br>Westmere, Northvale<br>PO Box 50172, Kingsford, 2031<br>South Africa
      <div class="contact">T:&nbsp; +27 (0)11 555 0142<br>www.<span class="entity--teal">korvel</span>.com</div>
    </div>
    <div class="footer-divider footer-divider--a"></div>
    <div class="footer-col footer-col--partner">
      <div class="entity--maroon">Korvel MB JV (Pty) Limited</div>
      27 Birch Street, Cnr Oakridge Avenue<br>Hillcrest Park,<br>Northvale 2188<br>South Africa
      <div class="contact"><span class="entity--maroon">T:</span> +27 (0)11 555 0198<br><span class="entity--maroon">www.</span>mabetagroup<span class="entity--maroon">.com</span></div>
    </div>
    <div class="footer-divider footer-divider--b"></div>
    <div class="footer-col footer-col--legal">
      Registration No. 2017/000000/07<br>Trading as Korvel MB JV (Pty) Limited
      <div class="directors">Directors: Peter Lang<span class="second">Simon</span></div>
    </div>
  </footer>
</div>
</body>
</html>
```